Business Card Design

I need a new business card design for myself. I am a life coach and therapist with both a private practice and now a newly formed business see both my websites: I am looking for a business card to support this and be close to the colours and design of my private practice website and my business website. I am looking for strong bright nature based colours. Sun, Sea and Greenery. The card should reflect inspiration, enlightenment, empowerment and strength!!!
www.helenagracewarrick.com and
www.calmer-paths-mentoring.co.uk
Updates
Thank you everyone for your designs. I will be making a final decision by the end of this week and will notify you as soon as possible after this.
Industry/Entity Type
Business
Contact Information for Business Card
Helena Grace Warrick, BSc, PGDip & MRes
Therapist and Life Coach
Calmer Paths Mentoring
17 Larkspur Road
Manchester
M4 7QT
0800 0619483 Mobile: 07700948216
email: hgwarrick@helenagracewarrick.com
Requirements
Must have
- not too busy. To be clear and easy to read information..
and to include this tag line:
"helping you live your life with passion and confidence"

```html
<!DOCTYPE html>
<html lang="en">
<head>
<meta charset="utf-8">
<title>Calmer Paths Mentoring – Business Card</title>
<link rel="stylesheet" href="https://fonts.googleapis.com/css2?family=Crimson+Pro:wght@400;500&display=swap">
<style>
  :root {
    --leaf: #5f9257;
    --forest: #2c6a33;
    --sea: #1fc1e6;
    --sun: #f4a022;
    --paper: #ffffff;
  }
  * { margin: 0; padding: 0; box-sizing: border-box; }
  html, body {
    width: 1200px;
    height: 791px;
    overflow: hidden;
    background: var(--paper);
  }
  .card {
    position: relative;
    width: 1200px;
    height: 791px;
    background: var(--paper);
    font-family: "Crimson Pro", "Palatino Linotype", Georgia, serif;
  }
  .brand-name {
    position: absolute;
    left: 55px;
    top: 214px;
    width: 410px;
    font-size: 56px;
    line-height: 62px;
    font-weight: 400;
    color: var(--leaf);
    text-align: right;
  }
  .colour-bands {
    position: absolute;
    left: 34px;
    top: 418px;
  }
  .tagline {
    position: absolute;
    left: 34px;
    top: 474px;
    width: 432px;
    font-size: 25px;
    line-height: 32px;
    color: var(--leaf);
  }
  .holder-name {
    position: absolute;
    left: 580px;
    top: 146px;
    font-size: 51px;
    line-height: 1;
    font-weight: 400;
    color: var(--leaf);
  }
  .qualifications {
    position: absolute;
    left: 580px;
    top: 206px;
    font-size: 40px;
    line-height: 1;
    color: var(--leaf);
  }
  .role {
    position: absolute;
    left: 580px;
    top: 290px;
    font-size: 50px;
    line-height: 1;
    color: var(--leaf);
  }
  .contact {
    position: absolute;
    left: 580px;
    top: 418px;
    font-size: 40px;
    line-height: 48px;
    color: var(--forest);
    font-style: normal;
  }
  .contact .email {
    font-size: 33px;
  }
</style>
</head>
<body>
  <main class="card">
    <div class="brand-name">Calmer Paths<br>Mentoring</div>

    <svg class="colour-bands" width="432" height="38" viewBox="0 0 432 38" aria-hidden="true">
      <rect x="0" y="0" width="124" height="37" fill="var(--leaf)"/>
      <rect x="127" y="0" width="175" height="37" fill="var(--sea)"/>
      <rect x="306" y="0" width="125" height="37" fill="var(--sun)"/>
    </svg>

    <p class="tagline">helping you live your life with passion and confidence</p>

    <h1 class="holder-name">Helena Grace Warrick,</h1>
    <p class="qualifications">BSc, PGDip &amp; MRes</p>
    <p class="role">Therapist and Life Coach</p>

    <address class="contact">
      17 Larkspur Road Manchester<br>
      M4 7QT 0800 0619483<br>
      Mobile: 07700948216<br>
      <span class="email">email: hgwarrick@helenagracewarrick.com</span>
    </address>
  </main>
</body>
</html>
```